Business card and stationery design

Harbour & Summit Planners is a leading event and conference design and management company.
Please view harbourandsummit.com.au

The business cards needs to convey:
- professionalism and competency
- exclusivity
- memorable experiences and quality

The business card needs to have the following aspects:
- double sided
- Full colour CMYK
- Printed on either high gloss matt card (designer to recommend)

For the business stationery we require:
- Letterhead with top banner and bottom footer
- A thank you card design
- a with compliments slip design
- a MS powerpoint and MS publisher client presentation slide design which includes cover page and then a standard presentation page
(Note- we do NOT require an envelope design- who sends letters these days!)

The company image is using the key colours of gold, silver and black.
A black background to the business card has been used before and is preferred although we are open to options.

Target Market(s)

High end corporations and businesses that require their events and conferences to be exceptionally well designed and managed

Industry/Entity Type

Business

Contact Information for Business Card

FRONT:

Darcy Whitlam
- Event and Conference Specialist

Mobile- +61 (0) 491 362 047
Office- 1300 586 917
darcyw@harbourandsummit.com.au

Web- harbourandsummit.com.au

BACK:

- Event and

Font styles to use
Other font styles liked:
• The logo designer used Trajan Pro Bold 3 for the font text in the logo

Requirements
Must have
• Amazing design of the following:
• - business card (double sided)
• - letterhead
• - client thank you card
• - powerpoint and publisher client presentation design files

```html
<!DOCTYPE html>
<html lang="en">
<head>
<meta charset="utf-8">
<title>Harbour &amp; Summit Planners – Business Card</title>
<link rel="stylesheet" href="https://fonts.googleapis.com/css2?family=Cinzel:wght@600&family=Open+Sans:wght@400;600&display=swap">
<style>
  :root {
    --backdrop: #e9e7e4;
    --card-charcoal: #3d3d3f;
    --card-silver: #a9a9ab;
    --silver-light: #c8c8ca;
    --gold: #e2b13c;
    --white: #f5f5f5;
    --text-soft: #e6e6e6;
  }
  * { box-sizing: border-box; margin: 0; padding: 0; }
  html, body {
    width: 1200px; height: 844px; overflow: hidden;
    background: var(--backdrop);
  }
  .canvas {
    position: relative; width: 1200px; height: 844px;
    display: flex; align-items: center; justify-content: center; gap: 60px;
  }
  .card {
    position: relative; width: 520px; height: 298px;
    border-radius: 3px; overflow: hidden;
    box-shadow: 0 10px 24px rgba(0,0,0,0.22);
  }

  /* Front */
  .card-front { background: var(--card-charcoal); }
  .front-brand {
    position: absolute; top: 44px; right: 34px;
    display: flex; align-items: center; gap: 12px;
  }
  .brand-dot {
    width: 44px; height: 44px; border-radius: 50%;
    background: var(--silver-light);
  }
  .brand-name {
    font-family: "Cinzel", serif; font-weight: 600;
    font-size: 17px; letter-spacing: 0.5px; color: var(--silver-light);
    line-height: 1.2; text-align: left; width: 170px;
  }
  .person { position: absolute; left: 34px; top: 132px; }
  .person-name {
    font-family: "Open Sans", sans-serif; font-weight: 600;
    font-size: 21px; color: var(--gold);
  }
  .person-title {
    font-family: "Open Sans", sans-serif; font-weight: 400;
    font-size: 14px; color: var(--text-soft); margin-top: 1px;
  }
  .contact-list {
    position: absolute; left: 34px; top: 196px;
    list-style: none;
    font-family: "Open Sans", sans-serif; font-size: 14px; color: var(--text-soft);
  }
  .contact-list li {
    display: flex; align-items: center; gap: 12px; height: 22px;
  }
  .contact-list svg { width: 13px; height: 13px; fill: var(--gold); flex: none; }

  /* Back */
  .card-back {
    background: radial-gradient(circle at 46% 40%, #cfcfd1 0%, var(--card-silver) 55%, #98989a 100%);
  }
  .back-pattern {
    position: absolute; inset: 0;
    background: radial-gradient(circle at 46% 40%, rgba(255,255,255,0.18) 0%, rgba(255,255,255,0) 60%);
  }
  .back-brand {
    position: absolute; right: 30px; bottom: 70px;
    font-family: "Cinzel", serif; font-weight: 600;
    font-size: 24px; letter-spacing: 0.5px; color: var(--white);
  }
</style>
</head>
<body>
<main class="canvas">

  <section class="card card-front" aria-label="Business card front">
    <div class="front-brand">
      <span class="brand-dot" aria-hidden="true"></span>
      <span class="brand-name">Harbour &amp; Summit Planners</span>
    </div>

    <div class="person">
      <p class="person-name">Darcy Whitlam</p>
      <p class="person-title">Event and Conference Specialist</p>
    </div>

    <ul class="contact-list">
      <li>
        <svg viewBox="0 0 16 16" aria-label="Mobile"><path d="M4 0h8a1 1 0 0 1 1 1v14a1 1 0 0 1-1 1H4a1 1 0 0 1-1-1V1a1 1 0 0 1 1-1zm1 2v10h6V2zm3 11a1 1 0 1 0 0 2 1 1 0 0 0 0-2z"/></svg>
        +61 (0) 491 362 047
      </li>
      <li>
        <svg viewBox="0 0 16 16" aria-label="Office phone"><path d="M3.6 1l2.5 3-1.5 2a9 9 0 0 0 5.4 5.4l2-1.5 3 2.5-1.6 2.6C7 15 1 9 1 2.6z"/></svg>
        1300 586 917
      </li>
      <li>
        <svg viewBox="0 0 16 16" aria-label="Email"><path d="M1 3h14v10H1zm1.5 1.2L8 8.6l5.5-4.4z"/></svg>
        darcyw@harbourandsummit.com.au
      </li>
      <li>
        <svg viewBox="0 0 16 16" aria-label="Website"><circle cx="8" cy="8" r="7"/></svg>
        www.harbourandsummit.com.au
      </li>
    </ul>
  </section>

  <section class="card card-back" aria-label="Business card back">
    <div class="back-pattern" role="img" aria-label="Soft silver background tone"></div>
    <p class="back-brand">Harbour &amp; Summit Planners</p>
  </section>

</main>
</body>
</html>
```